Design door hanger Bonaire Diving

We would like to have a design for a door hanger (See example below).
One side: Promote reef taster diving.
Other side: Promote Unlimited air/nitrox packages - lowest price guaranteed on Bonaire

We would like to inform people who rent a car with us about our air packages for diving. And non divers should be triggered to come and do a Reef Taster Dive with us. (KT Car rental and KT Dive is the same company.)

Target Market(s)

Divers and potential divers

Industry/Entity Type

Diving industry

Font styles to use
Sans Serif

Colors
0054AA
0677BA
7BADD7
CADEEF
E8F1F8
EE7325
F08F49
F5BC92
FAE3D3
FDF4ED

Requirements
Must have
• a few of the pictures included

```html
<!DOCTYPE html>
<html lang="en">
<head>
<meta charset="utf-8">
<title>KT Car Rental &amp; Dive – Door Hanger</title>
<link href="https://fonts.googleapis.com/css2?family=Montserrat:wght@400;500;700;800&family=Questrial&display=swap" rel="stylesheet">
<style>
  :root{
    --board-top:#6c6e6e;
    --board-bottom:#8c8f8e;
    --navy:#283562;
    --blue:#1066c2;
    --sky:#8ed3f5;
    --orange:#f5a623;
    --cream:#f3f0e3;
    --ink:#2a3a72;
    --white:#ffffff;
  }
  *{margin:0;padding:0;box-sizing:border-box;}
  html,body{width:1091px;height:1200px;overflow:hidden;}
  body{
    position:relative;
    background:linear-gradient(180deg,var(--board-top),var(--board-bottom));
    font-family:"Questrial",sans-serif;
    color:var(--ink);
  }
  .hanger-wrap{
    position:absolute;top:60px;width:382px;height:1020px;
    filter:drop-shadow(3px 5px 6px rgba(0,0,0,.35));
  }
  .hanger-wrap--front{left:132px;}
  .hanger-wrap--back{left:575px;}
  .hanger{
    position:relative;width:382px;height:1020px;overflow:hidden;background:var(--cream);
  }
  .hanger--front{
    clip-path:path('M0,1020 L0,335 C0,300 110,270 167,224 A73,73 0 1 0 127,177 C110,205 60,218 25,215 C8,213 0,200 0,185 L0,150 C0,60 90,0 200,0 L300,0 C345,0 382,35 382,80 L382,1020 Z');
  }
  .hanger--back{
    clip-path:path('M382,1020 L382,335 C382,300 272,270 215,224 A73,73 0 1 1 255,177 C272,205 322,218 357,215 C374,213 382,200 382,185 L382,150 C382,60 292,0 182,0 L82,0 C37,0 0,35 0,80 L0,1020 Z');
  }
  .photo{position:absolute;left:0;width:382px;}
  .photo--reef{top:0;height:220px;background:linear-gradient(135deg,#1e5a63 0%,#3f8a8c 45%,#6b7d6a 100%);}
  .photo--turtle{top:216px;height:250px;background:linear-gradient(180deg,#1c88b8 0%,#3aa5cf 50%,#8cc4d2 100%);}
  .photo--divers{top:0;height:470px;background:linear-gradient(180deg,#7fb6e4 0%,#3a9fc6 30%,#8fcfd6 42%,#e6e0d2 60%,#d8d1c2 100%);}
  .photo--gear{top:762px;height:190px;background:linear-gradient(180deg,#cfc7b8 0%,#6d6458 55%,#4e463d 100%);}
  .layer{position:absolute;left:0;top:0;width:382px;height:1020px;}
  .brand-badge{
    position:absolute;left:220px;top:341px;width:138px;height:138px;border-radius:50%;
    background:var(--white);border:4px solid var(--orange);
    display:flex;align-items:center;justify-content:center;text-align:center;
    font-family:"Montserrat",sans-serif;font-weight:700;font-size:17px;line-height:1.15;color:var(--navy);
  }
  .headline{position:absolute;left:31px;font-family:"Montserrat",sans-serif;line-height:1;}
  .headline__light{display:block;font-weight:500;color:var(--navy);}
  .headline__bold{display:block;font-weight:800;color:var(--blue);}
  .front-head{top:484px;}
  .front-head .headline__light{font-size:28px;}
  .front-head .headline__bold{font-size:40px;margin-top:4px;}
  .intro{position:absolute;left:31px;top:566px;width:340px;font-size:14px;line-height:1.2;color:var(--ink);}
  .ticks{position:absolute;left:31px;top:632px;width:340px;list-style:none;font-size:14px;line-height:1.2;}
  .ticks li{position:relative;padding-left:28px;margin-bottom:10px;}
  .ticks li::before{
    content:"";position:absolute;left:0;top:1px;width:16px;height:16px;border-radius:50%;background:var(--orange);
  }
  .ticks li::after{
    content:"";position:absolute;left:5px;top:4px;width:5px;height:8px;border:solid var(--navy);border-width:0 2px 2px 0;transform:rotate(40deg);
  }
  .thumb{position:absolute;border-radius:50%;}
  .thumb--worm{left:29px;top:834px;width:88px;height:88px;background:radial-gradient(circle,#8b3b4c,#2d2230);}
  .thumb--school{left:121px;top:817px;width:138px;height:138px;border:4px solid var(--cream);background:radial-gradient(circle,#9db6b8,#2b6a8a);}
  .thumb--seahorse{left:261px;top:833px;width:84px;height:84px;background:radial-gradient(circle,#b0603a,#1f5d7c);}
  .call{
    position:absolute;left:0;top:972px;width:382px;text-align:center;
    font-family:"Montserrat",sans-serif;font-weight:800;font-size:32px;color:var(--sky);letter-spacing:.5px;
  }
  .back-head{top:484px;left:29px;}
  .back-head .headline__light{font-size:32px;}
  .back-head .headline__bold{font-size:33px;margin-top:3px;}
  .back-head .headline__sub{display:block;font-weight:500;font-size:27px;color:var(--navy);margin-top:5px;}
  .dots{position:absolute;left:29px;top:602px;width:340px;list-style:none;font-size:15px;line-height:1.25;}
  .dots li{position:relative;padding-left:20px;margin-bottom:11px;}
  .dots li::before{
    content:"";position:absolute;left:0;top:5px;width:11px;height:11px;border-radius:50%;border:3px solid var(--orange);
  }
  .web-pill{
    position:absolute;left:81px;top:713px;width:220px;height:27px;border:1.5px solid var(--orange);border-radius:14px;
    text-align:center;line-height:24px;font-family:"Montserrat",sans-serif;font-weight:700;font-size:15px;color:var(--orange);
  }
  .side-label{
    position:absolute;font-size:14px;letter-spacing:1px;color:#2c2c2c;
    transform:rotate(-90deg);transform-origin:left top;
  }
  .side-label--front{left:98px;top:1080px;}
  .side-label--back{left:984px;top:1080px;}
  .caption{position:absolute;left:0;top:1127px;width:1091px;text-align:center;font-size:15px;letter-spacing:.6px;color:#1d1d1d;}
</style>
</head>
<body>

<div class="hanger-wrap hanger-wrap--front">
  <section class="hanger hanger--front">
    <div class="photo photo--reef" role="img" aria-label="Coral reef with tropical fish"></div>
    <div class="photo photo--turtle" role="img" aria-label="Sea turtle swimming over a sandy sea floor"></div>
    <svg class="layer" viewBox="0 0 382 1020" aria-hidden="true">
      <path d="M0,440 C80,470 160,478 240,462 C300,450 340,440 382,432 V1020 H0 Z" fill="var(--cream)"/>
    </svg>
    <div class="brand-badge">KT Car Rental<br>&amp; Dive</div>
    <h1 class="headline front-head">
      <span class="headline__light">REEF TASTER</span>
      <span class="headline__bold">DIVING</span>
    </h1>
    <p class="intro">Dive for the first time and enjoy our underwater paradise to the fullest under the guidance of an instructor. Give yourself a lifetime gift.</p>
    <ul class="ticks">
      <li>Ages 10 and up can sign up for our reef taster dive</li>
      <li>The Reef Taster Dive course will take 3-4 hours</li>
      <li>A group consists of a maximum of 4 people</li>
      <li>Experience the splendor of the ocean without much distraction by other divers</li>
      <li>Enjoy a lot of personal attention given by your instructor</li>
    </ul>
    <div class="thumb thumb--worm" role="img" aria-label="Close-up of a fireworm on the reef"></div>
    <div class="thumb thumb--school" role="img" aria-label="School of grunts swimming together"></div>
    <div class="thumb thumb--seahorse" role="img" aria-label="Seahorse holding on to the reef"></div>
    <svg class="layer" viewBox="0 0 382 1020" aria-hidden="true">
      <path d="M0,922 C80,900 150,922 230,912 C300,902 350,920 382,910 V924 C350,934 300,916 230,926 C150,936 80,916 0,936 Z" fill="var(--sky)"/>
      <path d="M0,936 C80,916 150,936 230,926 C300,916 350,934 382,924 V1020 H0 Z" fill="var(--navy)"/>
    </svg>
    <p class="call">Call +599 700 12 34</p>
  </section>
</div>

<div class="hanger-wrap hanger-wrap--back">
  <section class="hanger hanger--back">
    <div class="photo photo--divers" role="img" aria-label="Two divers in wetsuits chatting on a beach beside a white pickup"></div>
    <svg class="layer" viewBox="0 0 382 1020" aria-hidden="true">
      <path d="M0,440 C80,470 160,478 240,462 C300,450 340,440 382,432 V1020 H0 Z" fill="var(--cream)"/>
    </svg>
    <div class="brand-badge">KT Car Rental<br>&amp; Dive</div>
    <h2 class="headline back-head">
      <span class="headline__light">UNLIMITED</span>
      <span class="headline__bold">SUSTAINABLE AIR</span>
      <span class="headline__sub">AT A COMPETITIVE RATE</span>
    </h2>
    <ul class="dots">
      <li>KT Dive offers unlimited air/nitrox for the lowest price on Bonaire.</li>
      <li>We fill your tank up to 3200 PSI (220 BAR) without problem.</li>
    </ul>
    <p class="web-pill">www.ktcarrental.com</p>
    <div class="photo photo--gear" role="img" aria-label="Two scuba tanks with regulators and BCDs resting on a rock"></div>
    <svg class="layer" viewBox="0 0 382 1020" aria-hidden="true">
      <path d="M0,922 C80,900 150,922 230,912 C300,902 350,920 382,910 V924 C350,934 300,916 230,926 C150,936 80,916 0,936 Z" fill="var(--sky)"/>
      <path d="M0,936 C80,916 150,936 230,926 C300,916 350,934 382,924 V1020 H0 Z" fill="var(--navy)"/>
    </svg>
    <p class="call">Call +599 700 12 34</p>
  </section>
</div>

<p class="side-label side-label--front">SIDE 01</p>
<p class="side-label side-label--back">SIDE 02</p>
<p class="caption">Design Concept KT Car Rental &amp; Dive Door Hanger-03</p>

</body>
</html>
```